Elegant, High End Integrated Wellness Healthcare Practice

We need a brochure designed for an integrated mind-body wellness healthcare practice (www.larchveilclinic.com) . This brochure will be used when we cold call prospects (physicians to refer to our office, and potential consumers to utilize our services). Our practice is geographically located in the middle Tennessee USA region, although we have plans to become an international company as many of our offerings can be accessed anywhere in the world. Ultimately our goal is to have this brochure used as a leave-behind in an effort to introduce our integrated offerings to increase market share. The final product brochure should be both elegant and serious, with clean lines but also convey warmth and trust, as individuals who are coming for our services have usually struggled with their health for a significant amount of time before finding our practice.

The design brief was very specific about providing a high-end science-based 2-page brochure (not flier). Several designs submitted were fliers. The other designs were heavy on yoga or "woo woo" non-science-based looking pictures. This is a flier to appeal to physicians and other healthcare providers. Therefore the design must speak science and evidence-based methods of mind and body wellness care. I would also like to appeal to the other designers I paid extra for their submissions and who have indicated they will "respond in the coming days."

```html
<!DOCTYPE html>
<html lang="en">
<head>
<meta charset="utf-8">
<title>Larchveil Clinic Brochure</title>
<link href="https://fonts.googleapis.com/css2?family=Roboto+Condensed:wght@400;700&family=Cormorant+SC:wght@600&display=swap" rel="stylesheet">
<style>
  :root{
    --forest:#28391a;
    --leaf:#5b9431;
    --leaf-light:#7bb04a;
    --white:#ffffff;
    --ink:#1f2a14;
    --stage:#7f9a68;
  }
  *{margin:0;padding:0;box-sizing:border-box}
  html,body{width:952px;height:1200px;overflow:hidden}
  body{background:var(--stage);position:relative;font-family:"Roboto Condensed",Arial,sans-serif;color:var(--ink)}
  .page{position:absolute;left:102px;width:755px;height:533px;background:var(--white);overflow:hidden;box-shadow:0 6px 18px rgba(0,0,0,.25)}
  .page--cover{top:50px}
  .page--services{top:625px}
  .page svg.shapes{position:absolute;inset:0;width:755px;height:533px}
  .brand{position:absolute;left:588px;top:38px;width:134px;height:44px;background:var(--white);display:flex;align-items:center;gap:6px;padding:0 6px}
  .brand__dot{width:24px;height:24px;border-radius:50%;background:var(--leaf);flex:none}
  .brand__name{font-family:"Cormorant SC",Georgia,serif;font-weight:600;font-size:14px;line-height:1.05;color:var(--forest)}
  .contact{position:absolute;left:30px;top:432px;list-style:none;font-size:10px;line-height:13px;color:var(--ink)}
  .contact li{display:flex;align-items:center;gap:10px}
  .contact li.addr{margin-top:5px}
  .contact svg{width:8px;height:8px;flex:none}
  .web{position:absolute;left:0;top:489px;width:378px;height:20px;background:linear-gradient(90deg,var(--leaf),var(--leaf-light));color:var(--white);font-size:10px;display:flex;align-items:center;gap:11px;padding-left:30px}
  .web i{width:6px;height:6px;border-radius:50%;background:rgba(255,255,255,.6)}
  .headline{position:absolute;right:33px;top:396px;text-align:right;color:var(--white);font-weight:700;font-size:28px;line-height:32px;letter-spacing:.3px}
  .section-title{position:absolute;left:32px;top:30px;font-size:35px;font-weight:700;color:var(--forest);letter-spacing:.5px}
  .service-list{position:absolute;list-style:none;color:var(--ink)}
  .service-list--left{left:30px;top:353px;font-size:14px;line-height:18.3px}
  .service-list--left .gap{margin-top:9px}
  .service-list--right{left:390px;top:144px;font-size:16.5px;line-height:21.6px}
</style>
</head>
<body>

<section class="page page--cover">
  <svg class="shapes" viewBox="0 0 755 533" aria-hidden="false">
    <defs>
      <linearGradient id="consultPhoto" x1="0" y1="0" x2="1" y2="1">
        <stop offset="0" stop-color="#b9b2a6"/><stop offset=".5" stop-color="#d9dcdc"/><stop offset="1" stop-color="#c9c8c2"/>
      </linearGradient>
      <linearGradient id="leafArc" x1="0" y1="0" x2="1" y2="1">
        <stop offset="0" stop-color="#5b9431"/><stop offset="1" stop-color="#3f7224"/>
      </linearGradient>
      <clipPath id="lowerLeft"><rect x="0" y="240" width="378" height="293"/></clipPath>
    </defs>
    <rect x="378" y="0" width="377" height="533" fill="var(--forest)"/>
    <polygon points="0,0 135,0 0,322" fill="var(--forest)"/>
    <polygon points="650,0 755,0 755,320" fill="var(--leaf)"/>
    <circle cx="378" cy="150" r="268" fill="url(#leafArc)" clip-path="url(#lowerLeft)"/>
    <circle cx="378" cy="150" r="258" fill="var(--white)"/>
    <circle cx="378" cy="152" r="258" fill="none"/>
    <circle cx="378" cy="138" r="240" fill="url(#consultPhoto)" role="img" aria-label="Photo of a physician in a white coat consulting with a patient in a bright office"/>
  </svg>
  <div class="brand"><span class="brand__dot"></span><span class="brand__name">Larchveil<br>Clinic</span></div>
  <ul class="contact">
    <li><svg viewBox="0 0 10 10"><path d="M2 1l2 2-1 1.5c.8 1.5 1.5 2.2 3 3L7.5 6l2 2-1.5 1.5C5 9 1 5 .5 2.5z" fill="var(--ink)"/></svg>New Patients: (555) 240-7316</li>
    <li><svg viewBox="0 0 10 10"><path d="M2 1l2 2-1 1.5c.8 1.5 1.5 2.2 3 3L7.5 6l2 2-1.5 1.5C5 9 1 5 .5 2.5z" fill="var(--ink)"/></svg>Existing Patients: (555) 240-7382</li>
    <li class="addr"><svg viewBox="0 0 10 10"><path d="M5 0a3.5 3.5 0 0 0-3.5 3.5C1.5 6 5 10 5 10s3.5-4 3.5-6.5A3.5 3.5 0 0 0 5 0zm0 5a1.5 1.5 0 1 1 0-3 1.5 1.5 0 0 1 0 3z" fill="var(--ink)"/></svg>418 Alder Hollow Rd, Brenmoor, TN 37990, United States</li>
  </ul>
  <div class="web"><i></i>www.larchveilclinic.com</div>
  <h1 class="headline">DISCOVER<br>A BETTER WAY<br>TO A BETTER YOU</h1>
</section>

<section class="page page--services">
  <svg class="shapes" viewBox="0 0 755 533">
    <defs>
      <linearGradient id="herbPhoto" x1="0" y1="0" x2="1" y2="1">
        <stop offset="0" stop-color="#6d6254"/><stop offset=".5" stop-color="#9c8062"/><stop offset="1" stop-color="#5d5a4d"/>
      </linearGradient>
      <linearGradient id="brainPhoto" x1="0" y1="0" x2="1" y2="1">
        <stop offset="0" stop-color="#e7edf6"/><stop offset=".5" stop-color="#b9c8de"/><stop offset="1" stop-color="#7f95b4"/>
      </linearGradient>
      <clipPath id="herbFrame"><rect x="0" y="75" width="378" height="267"/></clipPath>
      <clipPath id="leftHalf"><rect x="0" y="0" width="378" height="533"/></clipPath>
    </defs>
    <rect x="378" y="0" width="377" height="533" fill="var(--forest)"/>
    <circle cx="378" cy="240" r="238" fill="var(--white)"/>
    <circle cx="378" cy="230" r="205" fill="url(#leafArc)" clip-path="url(#leftHalf)"/>
    <rect x="0" y="75" width="378" height="267" fill="url(#herbPhoto)" role="img" aria-label="Photo of herbal remedies, oils and a mortar on a wooden table"/>
    <circle cx="378" cy="230" r="205" fill="var(--leaf)" opacity=".78" clip-path="url(#herbFrame)"/>
    <circle cx="560" cy="72" r="42" fill="var(--leaf)" stroke="var(--white)" stroke-width="2"/>
    <circle cx="756" cy="152" r="13" fill="#0d0d0d"/>
    <circle cx="645" cy="420" r="160" fill="#5d6a52"/>
    <circle cx="650" cy="425" r="150" fill="url(#brainPhoto)" role="img" aria-label="Photo of a clinician interacting with a holographic brain scan display"/>
  </svg>
  <h2 class="section-title">SERVICES</h2>
  <ul class="service-list service-list--left">
    <li>&gt; Tonal Brain Care</li>
    <li>&gt; Functional Medicine</li>
    <li>&gt; Healthy Lifestyle Package</li>
    <li>&gt; Lightwave for Pain</li>
    <li class="gap">&gt; Wellness Package</li>
    <li>&gt; Mind Health</li>
    <li>&gt; Body Health</li>
    <li>&gt; Sleep Restoration</li>
  </ul>
  <ul class="service-list service-list--right">
    <li>&gt; Whole Body Wellness</li>
    <li>&gt; Nutrional Wellness</li>
    <li>&gt; 360° Integrative Wellness</li>
    <li>&gt; Brain Wave Mapping</li>
    <li>&gt; ADHD</li>
    <li>&gt; Stress Management</li>
    <li>&gt; Vitalbody Scan</li>
    <li>more...</li>
  </ul>
</section>

</body>
</html>
```